Say goodbye to Paper Cuts - Modern B2B Paper Ad

We need a design for a full page magazine ad

Company Overview:
FileNimbus is an administration support company for Northern Lending Insider. We are running a full page ad in Northern Lending Insider magazine

Ad Copy
"Say Goodbye to Paper Cuts"
"On-Demand Admin Support for Mortgage Professionals"
[website url at the bottom]

Ad Dimensions:
Trim: (w) 8.25” x (h) 10.875”
Bleed: (w) 8.75” x (h) 11.375”
Type: (w) 7.5” x (h) 10.125”

Ad Requirements (provided by the magazine)
Please supply all artwork in PC format only, either in EPS, Tiff or PDF format with the following requirements:

- All files must be 300 dpi high resolution with CMYK process colour.
- Any Pantone colours that are found will automatically be converted to CMYK. Please double check that all colours are in CMYK.
- EPS files must be in outline path for all fonts and embedded images.
- Tiff files must be in PC format, flatten with no layer.
- PDF files must be press optimized and embedded with images and fonts.
- All Double page ads and Full page ads must be in press-optimized PDF files.
- 0.125" bleed with crop marks are required for Double page ads, Full page ads and Panel ads to be supplied on artwork where specified.
- Ad files in Microsoft Word, Excel, PowerPoint or other software are NOT acceptable.
- Materials received should be in a printable file with no conversion required.

Industry/Entity Type

It Company

Font styles to use
Sans Serif

Requirements
Must have
• Bold, clean style

```html
<!DOCTYPE html>
<html lang="en">
<head>
<meta charset="utf-8">
<title>FileNimbus – Say Goodbye to Paper Cuts</title>
<link rel="stylesheet" href="https://fonts.googleapis.com/css2?family=Lato:wght@400;700;900&display=swap">
<style>
  :root {
    --brand-blue: #2a6fc0;
    --brand-blue-bright: #2f78cf;
    --brand-navy: #1d3461;
    --brand-ink: #1b2c50;
    --paper: #ffffff;
    --photo-light: #eef1f5;
    --photo-mid: #c9ced8;
  }
  * { margin: 0; padding: 0; box-sizing: border-box; }
  html, body {
    width: 848px;
    height: 1200px;
    overflow: hidden;
    background: var(--paper);
  }
  .ad {
    position: relative;
    width: 848px;
    height: 1200px;
    background: var(--paper);
    font-family: "Lato", sans-serif;
    overflow: hidden;
  }
  .ad__shapes {
    position: absolute;
    inset: 0;
  }
  .brand {
    position: absolute;
    top: 88px;
    left: 0;
    width: 100%;
    text-align: center;
    font-size: 76px;
    font-weight: 700;
    letter-spacing: -0.5px;
    color: var(--brand-ink);
    line-height: 1;
  }
  .headline {
    position: absolute;
    top: 872px;
    left: 0;
    width: 100%;
    text-align: center;
    color: var(--paper);
    font-weight: 700;
    font-size: 72px;
    line-height: 88px;
    letter-spacing: 0.5px;
    text-transform: uppercase;
  }
  .tagline {
    position: absolute;
    top: 1060px;
    left: 0;
    width: 100%;
    text-align: center;
    color: var(--paper);
    font-weight: 900;
    font-size: 19px;
    letter-spacing: 0.2px;
    text-transform: uppercase;
  }
  .website {
    position: absolute;
    top: 1124px;
    left: 0;
    width: 100%;
    text-align: center;
    color: var(--brand-ink);
    font-weight: 700;
    font-size: 18px;
    letter-spacing: 7px;
    text-transform: uppercase;
  }
</style>
</head>
<body>
<main class="ad">
  <svg class="ad__shapes" width="848" height="1200" viewBox="0 0 848 1200" xmlns="http://www.w3.org/2000/svg">
    <defs>
      <linearGradient id="footer-gradient" x1="0" y1="0" x2="0" y2="1">
        <stop offset="0" stop-color="#1f3a6b"/>
        <stop offset="1" stop-color="#2a6fc0"/>
      </linearGradient>
      <linearGradient id="photo-gradient" x1="0" y1="0" x2="0" y2="1">
        <stop offset="0" stop-color="#f3f5f8"/>
        <stop offset="0.45" stop-color="#cfd3db"/>
        <stop offset="1" stop-color="#4a4f5c"/>
      </linearGradient>
    </defs>

    <!-- header bands -->
    <rect class="band band--blue" x="0" y="204" width="848" height="31" fill="var(--brand-blue)"/>
    <polygon class="band band--navy" points="392,204 848,204 848,224 404,224" fill="var(--brand-navy)"/>

    <!-- left geometric panels -->
    <polygon class="panel panel--blue" points="0,235 139,235 190,465 0,465" fill="var(--brand-blue)"/>
    <polygon class="panel panel--navy" points="0,785 264,785 222,600" fill="var(--brand-navy)"/>
    <polygon class="panel-edge" points="112,300 130,300 266,802 248,802" fill="var(--brand-blue)"/>

    <!-- team photograph area -->
    <polygon class="team-photo" role="img" aria-label="Photograph of a smiling team of six business professionals in suits"
      points="139,235 848,235 848,802 266,802" fill="url(#photo-gradient)"/>

    <!-- footer -->
    <rect class="footer-bar" x="0" y="790" width="848" height="32" fill="var(--brand-blue-bright)"/>
    <rect class="footer-panel" x="0" y="822" width="848" height="378" fill="url(#footer-gradient)"/>
    <polygon class="url-strip" points="28,1100 812,1100 848,1200 0,1200" fill="var(--paper)"/>
  </svg>

  <div class="brand">FileNimbus</div>

  <h1 class="headline">Say Goodbye<br>to Paper Cuts</h1>
  <p class="tagline">On-Demand Admin Support for Mortgage Professionals</p>
  <p class="website">www.filenimbus.com</p>
</main>
</body>
</html>
```